Cleaning and Maintenance Business card design

i provide a service which includes;
Professional Window Cleaning
Lawn Mowing
Gardening
Painting
Rubbish Removal
Commercial Cleaning
Property & Ground Maintenance
Pensioner discounts apply
Call now for an inquiry and free quote
`Double sided` (willing to pay any extra)
i would like a design that is not too crowded and straight to the point.
i want the reader to know exactly what the business is about from one glance.
i would like the logo to communicate the businesses 3 main aspects (window cleaning, lawn mowing, and Cleaning)
Thanks.
Contact Information for Business Card
Business name : Brick 4 Leaf*
* with subline 'Windows, Lawns and Cleaning' (smaller font)
Name: Tom Varkonisky
Mobile: 0417 582 903
Email: t.varkonisky@mailbrook.net
ABN: 47 915 230 861
`Double Sided`
Logo Text
Brick 4 Leaf

```html
<!DOCTYPE html>
<html lang="en">
<head>
<meta charset="utf-8">
<title>Brick 4 Leaf – Business Card</title>
<link href="https://fonts.googleapis.com/css2?family=Questrial&family=Open+Sans:wght@600&display=swap" rel="stylesheet">
<style>
  :root {
    --backdrop: #c4c4c4;
    --card-dark: #000000;
    --card-light: #ffffff;
    --leaf-green: #b3d56f;
    --ink: #2e2e2e;
    --ink-soft: #3a3a3a;
    --white: #ffffff;
  }
  html, body {
    margin: 0;
    padding: 0;
    width: 1200px;
    height: 900px;
    overflow: hidden;
    background: var(--backdrop);
  }
  .canvas {
    position: relative;
    width: 1200px;
    height: 900px;
  }
  .card {
    position: absolute;
    width: 552px;
    height: 318px;
    box-sizing: border-box;
  }
  .card--front {
    left: 120px;
    top: 112px;
    background: var(--card-dark);
  }
  .brand-mark {
    position: absolute;
    left: 256px;
    top: 96px;
    width: 40px;
    height: 40px;
    background: var(--leaf-green);
  }
  .brand-name {
    position: absolute;
    left: 0;
    right: 0;
    top: 160px;
    margin: 0;
    text-align: center;
    font-family: "Questrial", sans-serif;
    font-weight: 400;
    font-size: 52px;
    line-height: 1;
    color: var(--white);
  }
  .brand-tagline {
    position: absolute;
    left: 0;
    right: 0;
    top: 224px;
    margin: 0;
    text-align: center;
    font-family: "Questrial", sans-serif;
    font-weight: 400;
    font-size: 17px;
    line-height: 1;
    color: var(--leaf-green);
  }
  .card--back {
    left: 536px;
    top: 450px;
    background: var(--card-light);
  }
  .accent-tab {
    position: absolute;
    left: 0;
    top: 120px;
    width: 42px;
    height: 156px;
    background: var(--leaf-green);
    border-radius: 0 10px 10px 0;
  }
  .contact {
    position: absolute;
    left: 54px;
    top: 143px;
    color: var(--ink-soft);
  }
  .contact-name {
    margin: 0 0 13px;
    font-family: "Open Sans", sans-serif;
    font-size: 22px;
    font-weight: 600;
    color: var(--ink);
    line-height: 1.2;
  }
  .contact-line {
    margin: 0;
    font-family: "Questrial", sans-serif;
    font-size: 20px;
    font-weight: 400;
    line-height: 26.5px;
  }
</style>
</head>
<body>
<main class="canvas">
  <section class="card card--front">
    <div class="brand-mark"></div>
    <h1 class="brand-name">Brick 4 Leaf</h1>
    <p class="brand-tagline">Windows, Lawns and Cleaning</p>
  </section>

  <section class="card card--back">
    <div class="accent-tab"></div>
    <div class="contact">
      <h2 class="contact-name">Tom Varkonisky</h2>
      <p class="contact-line">Mobile: 0417 582 903</p>
      <p class="contact-line">Email: t.varkonisky@mailbrook.net</p>
      <p class="contact-line">ABN: 47 915 230 861</p>
    </div>
  </section>
</main>
</body>
</html>
```